BRIM Outreach Partners Business Card Rebrand

Hello Designers! We are looking for help designing our new business card to go in conjunction with our company rebrand. Unfortunately, we have an event mid June that requires we get these printed ASAP (before our new website is launched.) We have a mostly complete Brand Book which I have uploaded to this request for your reference to company information, style, fonts. I've also enclosed our logo file in .eps & .jpg. Attached is a sample business card my boss liked but said was "too simple." I made it in Canva and do not profess to be a designer. NOT FOR DESIGN REFERENCE, ONLY FOR CONTEXT Here is what our old website looks like: https://brimoutreachpartners.com/.

```html
<!DOCTYPE html>
<html lang="en">
<head>
<meta charset="UTF-8">
<title>BRIM Outreach Partners – Business Card</title>
<link href="https://fonts.googleapis.com/css2?family=Poppins:wght@400;500;700;800&display=swap" rel="stylesheet">
<style>
  :root {
    --page-bg: #d9d9d9;
    --card-white: #ffffff;
    --brand-light: #7ec4ea;
    --brand-blue-start: #80c2e3;
    --brand-blue-end: #42a3d4;
    --ink: #0c0c0c;
    --ink-soft: #1d2a33;
    --paper: #ffffff;
  }
  * { box-sizing: border-box; margin: 0; padding: 0; }
  html, body { width: 1200px; height: 1200px; overflow: hidden; }
  body {
    background: var(--page-bg);
    font-family: 'Poppins', sans-serif;
    display: flex;
    flex-direction: column;
    align-items: center;
    justify-content: center;
    gap: 44px;
  }
  .card {
    position: relative;
    width: 900px;
    height: 514px;
    border-radius: 30px;
    overflow: hidden;
    box-shadow: 0 10px 24px rgba(0,0,0,0.18);
  }
  .card--front { background: var(--card-white); }
  .card--back {
    background: linear-gradient(100deg, var(--brand-blue-start) 0%, var(--brand-blue-end) 55%, var(--brand-blue-end) 100%);
  }
  .brand {
    position: absolute;
    left: 0; right: 0;
    display: flex;
    align-items: center;
    justify-content: center;
    gap: 26px;
  }
  .brand__dot { border-radius: 50%; flex: none; }
  .brand__name {
    font-weight: 700;
    color: var(--ink);
    line-height: 1.05;
    letter-spacing: 0.5px;
  }
  .card--front .brand { top: 150px; }
  .card--front .brand__dot { width: 150px; height: 150px; background: var(--brand-light); }
  .card--front .brand__name { font-size: 56px; }

  .social {
    position: absolute;
    left: 0; right: 0;
    bottom: 70px;
    display: flex;
    justify-content: center;
    align-items: center;
    gap: 14px;
    font-size: 22px;
    color: var(--ink);
  }
  .social__dot { width: 22px; height: 22px; border-radius: 50%; background: var(--brand-blue-end); }

  .card--back .brand { top: 40px; }
  .card--back .brand__dot { width: 130px; height: 130px; background: var(--paper); }
  .card--back .brand__name { font-size: 48px; }

  .holder { position: absolute; top: 212px; left: 0; right: 0; text-align: center; }
  .holder__name { font-size: 44px; font-weight: 800; color: var(--paper); line-height: 1.1; }
  .holder__title { font-size: 22px; color: var(--ink-soft); margin-top: 2px; }

  .divider { position: absolute; top: 318px; left: 70px; right: 70px; height: 2px; background: var(--paper); opacity: 0.9; }

  .contact {
    position: absolute;
    left: 70px; bottom: 48px;
    list-style: none;
    font-size: 22px;
    color: var(--ink-soft);
    line-height: 1.55;
  }
  .contact li { display: flex; align-items: center; gap: 14px; }
  .contact svg { width: 20px; height: 20px; fill: var(--paper); flex: none; }

  .address {
    position: absolute;
    right: 70px; top: 342px;
    text-align: right;
    font-size: 22px;
    line-height: 1.45;
    color: var(--ink);
    font-style: normal;
  }
</style>
</head>
<body>

  <section class="card card--front" aria-label="Business card front">
    <div class="brand">
      <span class="brand__dot"></span>
      <span class="brand__name">BRIM Outreach<br>Partners</span>
    </div>
    <div class="social">
      <span class="social__dot"></span>
      <span class="social__handle">@brim outreach partners</span>
    </div>
  </section>

  <section class="card card--back" aria-label="Business card back">
    <div class="brand">
      <span class="brand__dot"></span>
      <span class="brand__name">BRIM Outreach<br>Partners</span>
    </div>

    <div class="holder">
      <p class="holder__name">Dana Whitfield</p>
      <p class="holder__title">Attorney</p>
    </div>

    <div class="divider"></div>

    <ul class="contact">
      <li>
        <svg viewBox="0 0 24 24" aria-hidden="true"><path d="M6.6 10.8a15.1 15.1 0 0 0 6.6 6.6l2.2-2.2c.3-.3.7-.4 1-.2 1.1.4 2.3.6 3.6.6.6 0 1 .4 1 1V20c0 .6-.4 1-1 1A17 17 0 0 1 3 4c0-.6.4-1 1-1h3.5c.6 0 1 .4 1 1 0 1.3.2 2.5.6 3.6.1.3 0 .7-.2 1z"/></svg>
        555-014-2279
      </li>
      <li>
        <svg viewBox="0 0 24 24" aria-hidden="true"><path d="M2 5h20v14H2z M3.5 6.5 12 13l8.5-6.5" stroke="#42a3d4" stroke-width="1.5"/></svg>
        dana@brimoutreachpartners.com
      </li>
      <li>
        <svg viewBox="0 0 24 24" aria-hidden="true"><circle cx="12" cy="12" r="10"/><path d="M2 12h20M12 2c3 3 3 17 0 20M12 2c-3 3-3 17 0 20" stroke="#42a3d4" stroke-width="1.4" fill="none"/></svg>
        www.brimoutreachpartners.com
      </li>
    </ul>

    <address class="address">
      PO Box 40517,<br>Franklin,<br>TN 37064
    </address>
  </section>

</body>
</html>
```